IT Company, Needs new Logo and Letterhead Design

We need a Letterhead and possible a new logo for an existing IT Company. We are not happy with our current Letterhead that we are using in our quotes etc. We are happy to change our logo if required. We will upload our current logo and letterhead and look forward to getting some examples. We provide Server, Workstation and network support.

Target Market(s)

Small to Medium Sized Businesses.

Industry/Entity Type

It Company

Requirements
Must have
• Ability to edit the letterhead at a later date. Will need the source files for editing once approved.
Nice to have
• Same colour scheme, but we are open to suggestions.

```html
<!DOCTYPE html>
<html lang="en">
<head>
<meta charset="utf-8">
<title>Vantor Network Solutions – Letterhead</title>
<link rel="stylesheet" href="https://fonts.googleapis.com/css2?family=Arimo:wght@400;700&display=swap">
<style>
  :root {
    --brand-red: #d3050b;
    --ink: #111111;
    --band: #000000;
    --paper: #ffffff;
    --backdrop: #f6eeee;
    --watermark: rgba(211, 5, 11, 0.12);
    --watermark-ink: rgba(0, 0, 0, 0.14);
  }
  * { box-sizing: border-box; margin: 0; padding: 0; }
  html, body { width: 1200px; height: 1000px; overflow: hidden; }
  body {
    background: var(--backdrop);
    font-family: "Arimo", Arial, sans-serif;
    color: var(--ink);
    position: relative;
  }

  /* Letterhead sheet */
  .letterhead {
    position: absolute;
    left: 100px; top: 60px;
    width: 620px; height: 877px;
    background: var(--paper);
    box-shadow: 0 2px 10px rgba(0,0,0,0.18);
    display: flex; flex-direction: column;
  }
  .letterhead__top-band { height: 30px; background: var(--band); }
  .letterhead__header {
    display: flex; justify-content: space-between; align-items: flex-start;
    padding: 10px 26px 8px 26px;
    border-bottom: 4px solid var(--band);
    height: 66px;
  }
  .brand-small { display: flex; align-items: center; gap: 8px; margin-top: 8px; }
  .brand-small__square { width: 16px; height: 16px; background: var(--brand-red); }
  .brand-small__name { font-size: 17px; font-weight: 700; color: var(--brand-red); }
  .letterhead__title { font-size: 18px; margin-top: -4px; }

  .letterhead__body { flex: 1; position: relative; }
  .letterhead__watermark {
    position: absolute; left: 0; right: 0; bottom: 40px;
    text-align: center; font-size: 40px; font-weight: 700;
    color: var(--watermark-ink);
    display: flex; justify-content: center; align-items: center; gap: 14px;
  }
  .letterhead__watermark-square { width: 34px; height: 34px; background: var(--watermark); }

  .letterhead__footer {
    border-top: 5px solid var(--band);
    padding: 10px 26px 10px 26px;
    font-size: 10px;
    height: 74px;
  }
  .footer__phones { display: flex; justify-content: space-between; align-items: center; }
  .contact { display: flex; align-items: center; gap: 6px; font-weight: 700; }
  .contact svg { width: 12px; height: 12px; }
  .footer__address { margin: 6px 0 0 26px; line-height: 1.35; }
  .footer__address b { margin-right: 6px; }
  .footer__address-second { display: block; padding-left: 180px; }
  .letterhead__bottom-band { height: 24px; background: var(--band); }

  /* Brand lockup */
  .brand-lockup {
    position: absolute; left: 760px; top: 760px;
    display: flex; align-items: center; gap: 18px;
  }
  .brand-lockup__square { width: 44px; height: 44px; background: var(--brand-red); }
  .brand-lockup__name {
    font-size: 40px; font-weight: 700; color: var(--brand-red); line-height: 1.1;
  }
</style>
</head>
<body>

<article class="letterhead">
  <div class="letterhead__top-band"></div>
  <header class="letterhead__header">
    <div class="brand-small">
      <span class="brand-small__square"></span>
      <span class="brand-small__name">Vantor Network Solutions</span>
    </div>
    <h1 class="letterhead__title" style="font-weight:400">LetterHead</h1>
  </header>

  <div class="letterhead__body">
    <div class="letterhead__watermark" aria-hidden="true">
      <span class="letterhead__watermark-square"></span>
      <span>Vantor Network Solutions</span>
    </div>
  </div>

  <footer class="letterhead__footer">
    <div class="footer__phones">
      <span class="contact">
        <svg viewBox="0 0 12 12" aria-hidden="true"><rect x="3" y="0.5" width="6" height="11" rx="1" fill="#111"/><rect x="4" y="2" width="4" height="6" fill="#fff"/></svg>
        0400 218 647
      </span>
      <span class="contact">
        <svg viewBox="0 0 12 12" aria-hidden="true"><path d="M1 5 Q6 0 11 5 L9 6 L8 4 L4 4 L3 6 Z" fill="#111"/><rect x="2.5" y="6" width="7" height="5" rx="1" fill="#111"/></svg>
        1300 555 218
      </span>
    </div>
    <p class="footer__address">
      <b>Address:</b>P.O. BOX 2841, HARBOUR PLAZA, QLD 4000, 12 Ferncliff Street Brookfield
      <span class="footer__address-second">88 Tilden Street, Ashgrove</span>
    </p>
  </footer>
  <div class="letterhead__bottom-band"></div>
</article>

<div class="brand-lockup">
  <span class="brand-lockup__square"></span>
  <span class="brand-lockup__name">Vantor<br>Network Solutions</span>
</div>

</body>
</html>
```